Bramblewood Outings brochure

We need a brochure designed that is modern, high impact and grabs potential customers attention. I have provided a draft mock brochure as an example and to provide the desired information. The lay out and design can be changed.

The front to include image (examples provided. I may provide other images if I can source) Logo, Joining the Community, and perhaps a Community Access and Lifestyle Support Service, Specialising in Lifestyle and Recreation

Refer to website for information on the service www.bramblewoodoutings.com.au

Use colours of logo for design

Target Market(s)

CWPA participants (People with a disability and their family)

Colors

Designer to choose colors to be used in the design.

Requirements
Must have
• Image/s of people, logo, text in mock up design. Example images provided. Will source more images and upload.
Nice to have
• More than one image

```html
<!DOCTYPE html>
<html lang="en">
<head>
<meta charset="utf-8">
<title>Bramblewood Outings – Trifold Brochure</title>
<link rel="stylesheet" href="https://fonts.googleapis.com/css2?family=Open+Sans:ital,wght@0,400;0,600;0,700;0,800;1,400&family=Lora:ital,wght@1,600&display=swap">
<style>
:root{
  --bg:#e4e4e4;
  --green:#3fa535;
  --green-dark:#2b8a31;
  --green-light:#8cc63f;
  --lime:#b5dc6a;
  --white:#ffffff;
  --paper:#f6f7f5;
  --ink:#4a4a4a;
  --photo-a:#6f9a5a;
  --photo-b:#9bb8c9;
}
*{box-sizing:border-box;margin:0;padding:0}
html,body{width:1200px;height:2400px;overflow:hidden;background:var(--bg);font-family:"Open Sans",Arial,sans-serif;color:var(--ink)}
.canvas{position:relative;width:1200px;height:2400px}
.spread{position:absolute;left:60px;width:1080px;height:764px;box-shadow:0 18px 40px rgba(0,0,0,.22);background:var(--white);overflow:hidden}
.spread--outside{top:370px}
.spread--inside{top:1266px}
.panel{position:absolute;top:0;width:360px;height:764px;overflow:hidden}
.panel--1{left:0}.panel--2{left:360px}.panel--3{left:720px}
.panel-bg{position:absolute;inset:0;width:360px;height:764px}
.photo{position:absolute}
.green{background:var(--green)}
.paper{background:var(--paper)}
.tab{position:absolute;display:inline-block;background:var(--white);color:var(--green);font-weight:800;font-size:14px;letter-spacing:.06em;padding:6px 22px;border-radius:0 16px 16px 0}
.tab--green{background:var(--green);color:var(--white);border-radius:16px}
.tab--dark{background:var(--green-dark);color:var(--white)}
.body-copy{font-size:12.5px;line-height:1.55}
.body-copy--white{color:var(--white)}
.heading{font-weight:800;font-size:15px;color:var(--green);letter-spacing:.05em;text-transform:uppercase;margin-bottom:4px}
.rule{display:block;height:2px;width:150px;background:var(--green-light);margin:0 0 6px}
.brand-name{font-family:"Open Sans",Arial,sans-serif;font-weight:700;display:flex;align-items:center;gap:10px}
.brand-dot{width:30px;height:30px;border-radius:50%;flex:none}
.bullets{list-style:none}
.bullets li{position:relative;padding-left:18px;margin-bottom:3px}
.bullets li::before{content:"";position:absolute;left:2px;top:6px;width:8px;height:8px;border-radius:50%;background:var(--lime)}
.bullets--white li::before{background:var(--white)}
.tagline{font-family:"Lora",Georgia,serif;font-style:italic;font-weight:600;color:var(--lime);font-size:30px;line-height:1.05}
.service{color:var(--white);font-weight:700;font-size:21px;line-height:1.2;text-transform:uppercase}
.web{color:var(--lime);font-size:13.5px}
.contact-row{display:flex;align-items:center;gap:10px;font-size:13px;color:var(--green);margin-bottom:10px}
.contact-row svg{flex:none}
.round-photo{position:absolute;border-radius:50%;border:4px solid var(--white);box-shadow:0 0 0 3px var(--green)}
</style>
</head>
<body>
<main class="canvas">

  <!-- OUTSIDE -->
  <section class="spread spread--outside">

    <!-- About us -->
    <article class="panel panel--1 green">
      <span class="tab" style="top:28px;left:0">ABOUT US</span>
      <div class="body-copy body-copy--white" style="position:absolute;top:76px;left:34px;right:26px">
        <p style="font-style:italic;margin-bottom:12px">Bramblewood Outings is a service for people with an ongoing disability. We give support and assistance so people can connect with their local community in a way that is valued, safe and genuine, and we help every person lead a full life.</p>
        <p style="font-style:italic">Formed in 1997 by local families, the service became Bramblewood Outings in 2011 to reflect our focus on lifestyle and recreation support.</p>
      </div>
      <div class="photo" role="img" aria-label="Photo of a person in a wheelchair, hand on the wheel" style="top:400px;left:0;width:360px;height:364px;background:linear-gradient(160deg,#3b4a4f,#9aa3a0)"></div>
      <svg class="panel-bg" viewBox="0 0 360 764" aria-hidden="true" style="pointer-events:none">
        <path d="M0 380 C80 470 170 520 360 470 L360 0 L0 0Z" fill="var(--green)"/>
        <path d="M0 380 C80 470 170 520 360 470" fill="none" stroke="var(--white)" stroke-width="5"/>
        <path d="M210 764 C260 640 300 560 360 520 L360 764Z" fill="var(--green)"/>
        <path d="M210 764 C260 640 300 560 360 520" fill="none" stroke="var(--white)" stroke-width="4"/>
      </svg>
      <div class="round-photo" role="img" aria-label="Circular photo of a young person smiling in a wheelchair" style="top:450px;left:110px;width:110px;height:110px;background:linear-gradient(135deg,#8c6a55,#c9a58c)"></div>
    </article>

    <!-- Who we are / contact -->
    <article class="panel panel--2 paper">
      <div style="position:absolute;top:34px;left:40px;right:40px;text-align:center">
        <h3 class="heading">Who we are</h3>
        <p class="body-copy">A family driven lifestyle, recreation and leisure support service operated by a Management Committee consisting of parents and interested community members.</p>
        <h3 class="heading" style="margin-top:18px">How to apply</h3>
        <p class="body-copy">Please contact our office to discuss how Bramblewood Outings can support you.</p>
      </div>
      <div class="brand-name" style="position:absolute;top:300px;left:0;right:0;justify-content:center;color:var(--green);font-size:22px">
        <span class="brand-dot" style="background:var(--green-light)"></span>Bramblewood Outings
      </div>
      <span class="tab tab--green" style="top:368px;left:90px;width:180px;text-align:center">HOW TO FIND US</span>
      <div style="position:absolute;top:428px;left:52px;right:24px">
        <div class="contact-row" style="font-weight:700;font-size:17px">
          <svg width="22" height="22" viewBox="0 0 24 24"><path d="M6.6 10.8a15 15 0 006.6 6.6l2.2-2.2a1 1 0 011-.25 11.4 11.4 0 003.6.57 1 1 0 011 1V20a1 1 0 01-1 1A17 17 0 013 4a1 1 0 011-1h3.5a1 1 0 011 1c0 1.25.2 2.45.57 3.57a1 1 0 01-.25 1z" fill="var(--green)"/></svg>
          (07) 4000 1234
        </div>
        <div class="contact-row" style="font-size:12px">
          <svg width="22" height="22" viewBox="0 0 24 24"><rect x="2" y="5" width="20" height="14" rx="2" fill="var(--green)"/><path d="M3 6l9 7 9-7" fill="none" stroke="#fff" stroke-width="1.6"/></svg>
          hello@bramblewoodoutings.com.au
        </div>
        <div class="contact-row" style="color:var(--ink);font-size:14px;align-items:flex-start">
          <svg width="22" height="22" viewBox="0 0 24 24"><path d="M12 2a7 7 0 00-7 7c0 5 7 13 7 13s7-8 7-13a7 7 0 00-7-7zm0 9.5A2.5 2.5 0 1112 6.5a2.5 2.5 0 010 5z" fill="var(--green)"/></svg>
          <span>48–50 Wattle Street<br>Ferndale QLD 4870</span>
        </div>
        <div class="contact-row" style="color:var(--ink);font-size:13px">
          <svg width="22" height="22" viewBox="0 0 24 24"><circle cx="12" cy="12" r="10" fill="var(--green)"/></svg>
          bramblewoodoutings.com.au
        </div>
      </div>
    </article>

    <!-- Cover -->
    <article class="panel panel--3 green">
      <div class="photo" role="img" aria-label="Photo of a girl holding hands with a boy in a wheelchair wearing a helmet, in a park" style="top:0;left:0;width:360px;height:470px;background:linear-gradient(180deg,#4f7a3e 0%,#7fa36b 45%,#b9bfb3 100%)"></div>
      <svg class="panel-bg" viewBox="0 0 360 764" aria-hidden="true">
        <path d="M0 420 C120 500 250 500 360 390 L360 764 L0 764Z" fill="var(--green)"/>
        <path d="M0 420 C120 500 250 500 360 390" fill="none" stroke="var(--white)" stroke-width="6"/>
        <path d="M0 445 C120 525 250 520 360 420" fill="none" stroke="var(--green-light)" stroke-width="3"/>
      </svg>
      <div class="brand-name" style="position:absolute;top:26px;right:22px;color:var(--white);font-size:20px">
        <span class="brand-dot" style="border:3px solid var(--white)"></span>Bramblewood Outings
      </div>
      <div style="position:absolute;top:540px;left:34px;right:24px">
        <p class="tagline">“Joining the<br>Community</p>
        <p class="service" style="margin-top:14px">A Community Access<br>and Lifestyle<br>Support Service</p>
        <p class="web" style="margin-top:12px">www.bramblewoodoutings.com.au</p>
      </div>
    </article>
  </section>

  <!-- INSIDE -->
  <section class="spread spread--inside">

    <!-- Who we assist -->
    <article class="panel panel--1 green">
      <div class="photo" role="img" aria-label="Photo of a child on a parent's shoulders beside a person in a wheelchair, outdoors" style="top:0;left:0;width:360px;height:330px;background:linear-gradient(170deg,#6f9fcf 0%,#b8d3e6 55%,#d9a24c 100%)"></div>
      <svg class="panel-bg" viewBox="0 0 360 764" aria-hidden="true">
        <path d="M0 230 C90 330 220 350 360 300 L360 764 L0 764Z" fill="var(--green)"/>
        <path d="M0 230 C90 330 220 350 360 300" fill="none" stroke="var(--white)" stroke-width="5"/>
      </svg>
      <span class="tab tab--dark" style="top:352px;left:0">WHO WE ASSIST</span>
      <div class="body-copy body-copy--white" style="position:absolute;top:396px;left:30px;right:22px;font-size:12px">
        <p>People with a disability who:</p>
        <ul class="bullets bullets--white">
          <li>are over the age of 16 years;</li>
          <li>reside in the Ferndale region, from Riverbend to Sandy Cove;</li>
          <li>meet the State Disability Services eligibility criteria;</li>
          <li>are registered as Community Wellbeing Participant Access (CWPA) participants after rollout in July 2018; and/or</li>
          <li>have their own financial resources.</li>
        </ul>
        <h4 style="font-weight:800;font-size:14px;margin-top:14px">ROLE OF FAMILY/ADVOCATE</h4>
        <span class="rule" style="background:var(--white)"></span>
        <p>Families are our greatest resource and we actively seek their input to help the person with a disability maximise choice and control over their own lives.</p>
      </div>
    </article>

    <!-- Our philosophy -->
    <article class="panel panel--2 paper">
      <span class="tab tab--green" style="top:30px;left:24px">OUR PHILOSOPHY</span>
      <div class="body-copy" style="position:absolute;top:78px;left:30px;right:24px;font-size:12px">
        <h3 class="heading">Choice</h3><span class="rule"></span>
        <p style="margin-bottom:12px">Choice is a key element in lifestyle, recreation and leisure pursuits and we tailor support to meet people's personal plans and goals.</p>
        <h3 class="heading">Inclusion</h3><span class="rule"></span>
        <p style="margin-bottom:12px">We believe that supporting people individually is the best way to enable them to attain a valued role in their community.</p>
        <h3 class="heading">Opportunity</h3><span class="rule"></span>
        <p>All people have the right to be part of their community and to experience life's opportunities.</p>
      </div>
      <div class="photo" role="img" aria-label="Photo of a smiling woman talking on the phone at a desk with a laptop" style="top:470px;left:0;width:360px;height:294px;background:linear-gradient(150deg,#cfd3d6,#7d8a96)"></div>
      <svg class="panel-bg" viewBox="0 0 360 764" aria-hidden="true">
        <path d="M0 470 L0 440 C120 500 240 520 360 480 L360 470Z" fill="var(--paper)"/>
        <path d="M0 440 C120 500 240 520 360 480" fill="none" stroke="var(--green)" stroke-width="5"/>
        <path d="M260 764 C300 680 330 640 360 620 L360 764Z" fill="var(--green)"/>
      </svg>
      <div class="round-photo" role="img" aria-label="Circular photo of a smiling couple" style="top:410px;left:248px;width:96px;height:96px;background:linear-gradient(135deg,#9b7a63,#dcc0a8)"></div>
    </article>

    <!-- How we assist -->
    <article class="panel panel--3 green">
      <span class="tab" style="top:30px;left:0">HOW WE ASSIST</span>
      <div class="body-copy body-copy--white" style="position:absolute;top:76px;left:30px;right:24px;font-size:12px">
        <p>We assist people to:</p>
        <ul class="bullets bullets--white" style="margin:4px 0 14px">
          <li>pursue individual interests;</li>
          <li>develop social and community skills;</li>
          <li>participate in daily living activities;</li>
          <li>take part in sport and recreation;</li>
          <li>build confidence and self-esteem;</li>
          <li>keep and strengthen friendships;</li>
          <li>reach work and learning goals;</li>
          <li>access local services and events;</li>
          <li>improve health and wellbeing;</li>
          <li>achieve their goals and desired outcomes.</li>
        </ul>
        <p>We employ support people to assist individuals in a range of settings:</p>
        <ul class="bullets bullets--white" style="margin:4px 0 16px">
          <li>one to one support;</li>
          <li>in their home and in general community settings;</li>
          <li>to implement their personal plan;</li>
          <li>to access community services; and</li>
          <li>to meet their changing needs.</li>
        </ul>
        <p style="text-align:center;padding:0 20px">We can provide 24-hour support but all support is in non-congregated settings.</p>
      </div>
      <div class="brand-name" style="position:absolute;bottom:44px;right:30px;color:var(--white);font-size:19px">
        <span class="brand-dot" style="border:3px solid var(--white)"></span>Bramblewood Outings
      </div>
    </article>
  </section>

</main>
</body>
</html>
```